FH banner

we need a banner design (36"x120" horizontal) that will be displayed on a local high school baseball field. My company ( Orbit Print Co) has been producing signage for the Fern Hollow community since 2009. We would like to communicate that we do more than banners. The final design should include the slogan "Signs Shirts Swag" and our Logo.

Target Market(s)

companies, teams, events, shirt and other marketing items.

Industry/Entity Type

Sign, Print,

Font styles to use
Sans Serif

Requirements
Should not have
• no baseball content.

```html
<!DOCTYPE html>
<html lang="en">
<head>
<meta charset="utf-8">
<title>Orbit Print Co — Field Banner</title>
<link href="https://fonts.googleapis.com/css2?family=Gochi+Hand&family=Montserrat:wght@800&display=swap" rel="stylesheet">
<style>
  :root {
    --page: #ffffff;
    --banner: #000000;
    --cyan: #1ea3dc;
    --blue: #1466c0;
    --navy: #2a2f8f;
    --white: #ffffff;
    --ink: #111111;
    --glow: #2f8fe0;
  }
  html, body {
    margin: 0;
    width: 1194px;
    height: 1200px;
    overflow: hidden;
    background: var(--page);
  }
  .banner {
    position: absolute;
    left: 37px;
    top: 432px;
    width: 1120px;
    height: 335px;
    background:
      radial-gradient(ellipse 260px 120px at 330px 335px, rgba(30,120,200,0.22), transparent 70%),
      radial-gradient(ellipse 300px 140px at 700px 0px, rgba(40,60,160,0.18), transparent 70%),
      radial-gradient(ellipse 220px 160px at 1100px 300px, rgba(30,140,210,0.2), transparent 70%),
      radial-gradient(ellipse 200px 200px at 40px 80px, rgba(40,80,170,0.14), transparent 70%),
      var(--banner);
    overflow: hidden;
  }
  .banner-pattern { position: absolute; inset: 0; }
  .logo-badge { position: absolute; left: 34px; top: 29px; width: 298px; height: 298px; }
  .logo-name {
    position: absolute;
    left: 68px; top: 63px;
    width: 230px; height: 230px;
    display: flex; align-items: center; justify-content: center;
    text-align: center;
    font-family: "Montserrat", sans-serif;
    font-weight: 800;
    font-size: 34px;
    line-height: 1.05;
    color: var(--ink);
    text-transform: uppercase;
  }
  .service-badge { position: absolute; width: 136px; height: 136px; }
  .service-word {
    position: absolute;
    top: 190px;
    font-family: "Gochi Hand", sans-serif;
    font-size: 78px;
    line-height: 1;
    color: var(--white);
    text-shadow: 2px 2px 0 var(--glow), -1px -1px 0 var(--glow), 0 0 4px var(--glow);
    transform: translateX(-50%);
    white-space: nowrap;
  }
  .divider {
    position: absolute;
    top: 203px;
    width: 1.5px;
    height: 90px;
    background: var(--white);
  }
</style>
</head>
<body>
  <div class="banner">
    <svg class="banner-pattern" width="1120" height="335" viewBox="0 0 1120 335" role="img" aria-label="Fine flowing blue line waves across black background">
      <defs>
        <linearGradient id="wave" x1="0" y1="0" x2="1" y2="0">
          <stop offset="0" stop-color="#1ea3dc" stop-opacity="0"/>
          <stop offset="0.5" stop-color="#1e7fd0" stop-opacity="0.35"/>
          <stop offset="1" stop-color="#2a2f8f" stop-opacity="0"/>
        </linearGradient>
      </defs>
      <path d="M80 335 Q330 230 640 300" fill="none" stroke="url(#wave)" stroke-width="10"/>
      <path d="M520 0 Q700 140 930 20" fill="none" stroke="url(#wave)" stroke-width="10"/>
      <path d="M880 335 Q1000 200 1120 190" fill="none" stroke="url(#wave)" stroke-width="10"/>
    </svg>

    <svg class="logo-badge" viewBox="0 0 298 298">
      <defs>
        <linearGradient id="ring" x1="0" y1="0" x2="0" y2="1">
          <stop offset="0" stop-color="#1ea3dc"/>
          <stop offset="0.6" stop-color="#1466c0"/>
          <stop offset="1" stop-color="#2a2f8f"/>
        </linearGradient>
      </defs>
      <circle cx="149" cy="149" r="146" fill="url(#ring)"/>
      <circle cx="149" cy="151" r="134" fill="#000"/>
      <circle cx="149" cy="149" r="122" fill="url(#ring)"/>
      <circle cx="149" cy="149" r="115" fill="#f3f1f0"/>
    </svg>
    <div class="logo-name">Orbit<br>Print Co</div>

    <svg class="service-badge" style="left:385px;top:51px" viewBox="0 0 136 136" role="img" aria-label="Line icon of a sign board and hanging sign">
      <circle cx="68" cy="68" r="62" fill="none" stroke="url(#svc)" stroke-width="4"/>
      <defs><linearGradient id="svc" x1="0" y1="0" x2="0" y2="1"><stop offset="0" stop-color="#1ea3dc"/><stop offset="1" stop-color="#2a2f8f"/></linearGradient></defs>
      <circle cx="68" cy="68" r="44" fill="#0d2a55"/>
    </svg>
    <svg class="service-badge" style="left:649px;top:48px" viewBox="0 0 136 136" role="img" aria-label="Line icon of two t-shirts">
      <circle cx="68" cy="68" r="62" fill="none" stroke="url(#svc)" stroke-width="4"/>
      <circle cx="68" cy="68" r="44" fill="#0d2a55"/>
    </svg>
    <svg class="service-badge" style="left:912px;top:51px" viewBox="0 0 136 136" role="img" aria-label="Line icon of a cap, mug and tote bag">
      <circle cx="68" cy="68" r="62" fill="none" stroke="url(#svc)" stroke-width="4"/>
      <circle cx="68" cy="68" r="44" fill="#0d2a55"/>
    </svg>

    <div class="service-word" style="left:453px">Signs</div>
    <div class="divider" style="left:579px"></div>
    <div class="service-word" style="left:717px">Shirts</div>
    <div class="divider" style="left:859px"></div>
    <div class="service-word" style="left:985px">Swag</div>
  </div>
</body>
</html>
```